Business Card Design

Please use the Logo for colors and styles, and create a business card using the following info:

Matthias Lorbeer
Web Developer

Lorbeer Systems
+41 76 418 57 90
matthias@lorbeer-systems.ch
www.lorbeer-systems.ch

Download the logo at http://lorbeer-systems.ch/tl_files/lorbeer_systems.zip

Thanks for your works!

```html
<!DOCTYPE html>
<html lang="en">
<head>
<meta charset="utf-8">
<title>Lorbeer Systems – Business Card</title>
<link rel="stylesheet" href="https://fonts.googleapis.com/css2?family=Carlito:wght@400;700&family=Cinzel:wght@400;600&display=swap">
<style>
  :root {
    --backdrop: #ecebe8;
    --card: #ffffff;
    --brand-blue: #1f6aa8;
    --ink: #1b1b1b;
    --ink-soft: #2a2a2a;
    --rule: #3a3a3a;
    --card-shadow: rgba(0, 0, 0, 0.18);
  }
  * { box-sizing: border-box; margin: 0; padding: 0; }
  html, body {
    width: 1200px;
    height: 900px;
    overflow: hidden;
    background: var(--backdrop);
  }
  .sheet {
    position: relative;
    width: 1200px;
    height: 900px;
  }
  .card {
    position: absolute;
    top: 297px;
    width: 520px;
    height: 306px;
    background: var(--card);
    box-shadow: 0 6px 18px var(--card-shadow);
    overflow: hidden;
  }
  .card--front { left: 60px; }
  .card--back { left: 620px; }

  .brand {
    position: absolute;
    left: 27px;
    top: 30px;
    font-family: "Carlito", "Calibri", sans-serif;
    font-weight: 700;
    font-size: 29px;
    letter-spacing: 0.5px;
    color: var(--brand-blue);
    text-transform: uppercase;
  }

  .contact {
    position: absolute;
    left: 27px;
    bottom: 32px;
    list-style: none;
    font-family: "Carlito", "Calibri", sans-serif;
    font-size: 13.5px;
    line-height: 16px;
    color: var(--ink-soft);
  }

  .identity {
    position: absolute;
    right: 28px;
    bottom: 30px;
    text-align: center;
    font-family: "Cinzel", "Trajan Pro", serif;
    color: var(--ink);
  }
  .identity__name {
    font-size: 21px;
    font-weight: 600;
    letter-spacing: 0.5px;
    padding: 0 2px 2px;
    border-bottom: 1.5px solid var(--rule);
  }
  .identity__role {
    margin-top: 4px;
    font-size: 12.5px;
    letter-spacing: 4.6px;
  }

  .card__url {
    position: absolute;
    left: 0;
    right: 0;
    top: 50%;
    transform: translateY(-50%);
    text-align: center;
    font-family: "Carlito", "Calibri", sans-serif;
    font-size: 25px;
    color: var(--ink);
  }
</style>
</head>
<body>
  <main class="sheet">
    <section class="card card--front" aria-label="Business card front">
      <div class="brand">Lorbeer Systems</div>
      <ul class="contact">
        <li>+41 76 418 57 90</li>
        <li>matthias@lorbeer-systems.ch</li>
        <li>www.lorbeer-systems.ch</li>
      </ul>
      <div class="identity">
        <div class="identity__name">Matthias Lorbeer</div>
        <div class="identity__role">WEB DEVELOPER</div>
      </div>
    </section>

    <section class="card card--back" aria-label="Business card back">
      <p class="card__url">www.lorbeer-systems.ch</p>
    </section>
  </main>
</body>
</html>
```